New custom software business needs a Wordpress site

We need a Wordpress site for a new company based out of Chicago called 'Vellora Consulting'. Using a mix of on and off-shore resources we build custom software solutions, mainly focusing on small to medium sized companies. We help our customers "aspire" to do great things.
We have a basic site up here: https://brindlewave.example/. We worked on the content for it but not the branding. For now, this houses all the pages (except for a Contact Us page we'll be adding soon) for the foreseeable future.
We also have a new logo (attached) that we'd like to base the styling/colors on.
Target Market(s)
Small to medium sized companies that require tech resources
Industry/Entity Type
Software
Nice to have
- Teamwork, tech, professional but not elitist

```html
<!DOCTYPE html>
<html lang="en">
<head>
<meta charset="utf-8">
<title>Vellora Consulting</title>
<link rel="stylesheet" href="https://fonts.googleapis.com/css2?family=Orbitron:wght@500;600&family=Exo+2:wght@500;600;700&family=Roboto:ital,wght@0,400;0,500;1,400&display=swap">
<style>
:root{
  --blue:#0b4db2;
  --blue-deep:#083f9a;
  --blue-band:#1a6ad6;
  --blue-light:#4a8ac8;
  --blue-pale:#8fb6e6;
  --sky-dark:#2c3e55;
  --sky-mid:#5d7590;
  --text:#555b63;
  --heading:#0b4db2;
  --white:#ffffff;
}
*{margin:0;padding:0;box-sizing:border-box}
html,body{width:1200px;height:4376px;overflow:hidden;background:var(--white)}
body{font-family:"Roboto",sans-serif;color:var(--text)}
.page{position:relative;width:1200px;height:4376px;overflow:hidden}
.abs{position:absolute}
.shapes{position:absolute;left:0;top:0}
.display{font-family:"Orbitron",sans-serif;font-weight:500;letter-spacing:2px;text-transform:uppercase}

/* header */
.brand{left:153px;top:48px;display:flex;align-items:center;gap:12px;color:var(--white);font-family:"Exo 2",sans-serif;font-weight:600;font-size:22px;letter-spacing:1px}
.brand-dot{width:40px;height:40px;border-radius:50%;background:var(--white)}
.nav{left:435px;top:41px;width:612px;height:53px;border-radius:27px;background:var(--blue);display:flex;align-items:center;justify-content:space-evenly;padding:0 16px}
.nav a{color:var(--white);text-decoration:none;font-family:"Exo 2",sans-serif;font-weight:500;font-size:15px;letter-spacing:.5px}
.hero-title{left:0;top:246px;width:1200px;text-align:center;color:var(--white);font-size:42px;line-height:62px}
.hero-sub{left:0;top:384px;width:1200px;text-align:center;color:var(--white);font-family:"Exo 2",sans-serif;font-size:18px;line-height:22px;letter-spacing:.5px}

/* section headings */
.section-title{left:0;width:1200px;text-align:center;color:var(--heading);font-size:37px}
.section-title.on-blue{color:var(--white)}
.body-copy{font-size:14.5px;line-height:20.5px}
.about-copy{left:210px;top:903px;width:780px;text-align:center}
.about-copy p+p{margin-top:20.5px}

.btn{display:flex;align-items:center;justify-content:center;gap:10px;height:47px;width:170px;border-radius:24px;background:var(--blue);color:var(--white);font-family:"Orbitron",sans-serif;font-size:13px;letter-spacing:1.5px;text-transform:uppercase}
.btn-dot{width:24px;height:24px;border-radius:50%;border:2px solid var(--white)}

/* services */
.service-card{top:1584px;width:288px;height:362px;background:var(--white);box-shadow:0 4px 14px rgba(0,0,0,.18);text-align:center;padding-top:24px}
.service-icon{width:112px;height:112px;border-radius:50%;margin:0 auto;border:3px solid var(--blue);background:radial-gradient(circle,var(--blue) 0 46px,var(--white) 47px)}
.service-name{margin-top:18px;font-family:"Exo 2",sans-serif;font-weight:600;font-size:19px;line-height:24px;color:#333a44;padding:0 40px}
.service-text{margin-top:24px;font-size:12.5px;line-height:19px;color:#777;padding:0 30px}

/* why */
.why-frame{left:114px;top:2050px;width:117px;height:129px;border:4px solid var(--blue-light)}
.why-photo{left:141px;top:2074px;width:362px;height:404px;background:linear-gradient(135deg,#d9dfe6,#8ea5bd 55%,#5a7390)}
.why-title{left:552px;top:2088px;color:var(--heading);font-size:37px}
.why-copy{left:552px;top:2166px;width:510px}
.why-copy p+p{margin-top:20.5px}

/* testimonial */
.quote-mark{left:0;top:2640px;width:1200px;text-align:center;color:var(--white);font-family:"Exo 2",sans-serif;font-weight:700;font-size:110px;line-height:90px}
.quote-text{left:220px;top:2738px;width:760px;text-align:center;color:var(--white);font-style:italic;font-size:26px;line-height:33px}
.avatar{left:459px;top:2857px;width:92px;height:92px;border-radius:50%;border:3px solid var(--white);background:linear-gradient(160deg,#9c8a78,#4a3c33)}
.person{left:569px;top:2876px;color:var(--white);font-family:"Exo 2",sans-serif}
.person strong{display:block;font-weight:600;font-size:17px}
.person span{font-size:13px}

/* blog */
.post-feature{left:146px;top:3332px;width:480px;height:371px;background:linear-gradient(160deg,#8fa3b8,#3f5570 60%,#1f2f45)}
.post-feature h3{position:absolute;left:38px;bottom:58px;width:420px;color:var(--white);font-family:"Exo 2",sans-serif;font-weight:700;font-size:24px;line-height:31px}
.post-small{left:648px;width:401px;height:177px;display:flex}
.post-photo{width:195px;height:100%;background:linear-gradient(150deg,#b9c3cc,#56677a)}
.post-text{flex:1;background:var(--blue-pale);padding:20px 14px 0 14px;color:var(--white)}
.post-text h4{font-family:"Exo 2",sans-serif;font-weight:700;font-size:14.5px;line-height:17.5px}
.post-text p{margin-top:10px;font-size:10.5px;line-height:13px}

/* footer */
.footer-brand{left:140px;top:4110px;width:260px;text-align:center;color:var(--white)}
.footer-brand .mark{width:110px;height:110px;border-radius:50%;background:var(--blue-light);margin:0 auto 22px}
.footer-brand .name{font-family:"Exo 2",sans-serif;font-weight:600;font-size:24px;letter-spacing:2px;text-transform:uppercase}
.footer-col{top:4050px;color:var(--white)}
.footer-col h5{font-family:"Orbitron",sans-serif;font-weight:500;font-size:20px;letter-spacing:1.5px;text-transform:uppercase;margin-bottom:14px}
.footer-col li{list-style:none;font-size:11.5px;line-height:25px}
.social{left:910px;top:4166px;display:flex;gap:14px}
.social span{width:22px;height:22px;border-radius:50%;background:var(--white)}
.footer-rule{left:153px;top:4294px;width:894px;height:1px;background:rgba(255,255,255,.35)}
.copyright{left:0;top:4324px;width:1200px;text-align:center;color:var(--white);font-size:11.5px}
</style>
</head>
<body>
<div class="page">

  <svg class="shapes" width="1200" height="4376" viewBox="0 0 1200 4376" aria-hidden="true">
    <defs>
      <linearGradient id="sky" x1="0" y1="0" x2="0" y2="1">
        <stop offset="0" stop-color="#26364b"/>
        <stop offset=".55" stop-color="#4f6885"/>
        <stop offset="1" stop-color="#7d93aa"/>
      </linearGradient>
      <linearGradient id="band" x1="0" y1="0" x2="1" y2="0">
        <stop offset="0" stop-color="#4a8ac8"/>
        <stop offset=".5" stop-color="#2b6dc0"/>
        <stop offset="1" stop-color="#4a8ac8"/>
      </linearGradient>
    </defs>
    <!-- hero -->
    <polygon points="0,0 1200,0 1200,527 600,652 0,527" fill="url(#sky)"/>
    <polygon points="34,544 600,655 1166,544 600,705" fill="url(#band)"/>
    <!-- services -->
    <polygon points="34,1462 600,1295 1166,1462 600,1351" fill="url(#band)"/>
    <polygon points="0,1479 600,1351 1200,1479 1200,1773 0,1773" fill="#0b4db2"/>
    <!-- testimonial -->
    <polygon points="0,2604 1200,2604 1200,2941 600,3040 0,2941" fill="#1a6ad6"/>
    <polygon points="34,2950 600,3040 1166,2950 600,3080" fill="#0b48a8"/>
    <!-- footer -->
    <polygon points="34,4010 600,3845 1166,4010 600,3900" fill="url(#band)"/>
    <polygon points="0,4025 600,3900 1200,4025 1200,4376 0,4376" fill="#083f9a"/>
  </svg>

  <!-- header -->
  <div class="abs" role="img" aria-label="Low-angle photo of glass office towers against the sky" style="left:0;top:0;width:1px;height:1px"></div>
  <div class="abs brand"><span class="brand-dot"></span>Vellora Consulting</div>
  <nav class="abs nav">
    <a href="#">HOME</a><a href="#">SERVICES</a><a href="#">WHY VELLORA?</a><a href="#">VELLORA LEADERSHIP</a>
  </nav>
  <h1 class="abs hero-title display">Welcome to<br>Vellora Consulting</h1>
  <p class="abs hero-sub">Software consulting company specializing in serving<br>small to medium size businesses.</p>

  <!-- about -->
  <h2 class="abs section-title display" style="top:818px">About Us</h2>
  <div class="abs about-copy body-copy">
    <p>Welcome to Vellora, a software consulting company specializing in serving small to medium size businesses. We understand the unique challenges and opportunities that these companies face, and we are dedicated to helping them succeed through innovative technology solutions.</p>
    <p>Our team of experienced professionals has a diverse range of skills and expertise, making us well-equipped to handle any project, big or small. We specialize in custom software development, working closely with our clients to understand their specific needs and build solutions that meet their requirements.</p>
    <p>From developing web and mobile applications to implementing cloud-based systems and integrating with existing platforms, we have the tools and knowledge to deliver results that drive success. We also offer a range of other services, including IT consulting, project management, and technical support, to help businesses optimize their operations and achieve their goals.</p>
  </div>
  <a class="abs btn" style="left:515px;top:1185px"><span class="btn-dot"></span>Read More</a>

  <!-- services -->
  <h2 class="abs section-title on-blue display" style="top:1490px">Our Services</h2>
  <div class="abs service-card" style="left:151px">
    <div class="service-icon" role="img" aria-label="Puzzle-piece icon"></div>
    <div class="service-name">Custom Solution Delivery</div>
    <p class="service-text">Vellora offers a range of services focused on helping businesses and organizations deliver software solutions to their customers or users.</p>
  </div>
  <div class="abs service-card" style="left:456px">
    <div class="service-icon" role="img" aria-label="Team of people icon"></div>
    <div class="service-name">Staff Augmentation</div>
    <p class="service-text">Let Vellora help you supplement your existing software development teams with additional resources and expertise. We provided access to experienced</p>
  </div>
  <div class="abs service-card" style="left:762px">
    <div class="service-icon" role="img" aria-label="Code on a monitor icon"></div>
    <div class="service-name">Custom Software Solutions</div>
    <p class="service-text">Vellora offers a range of services focused on helping businesses and organizations deliver software solutions to their customers or users.</p>
  </div>

  <!-- why -->
  <div class="abs why-frame"></div>
  <div class="abs why-photo" role="img" aria-label="Photo of two businessmen shaking hands in an office"></div>
  <h2 class="abs why-title display">Why Vellora?</h2>
  <div class="abs why-copy body-copy">
    <p>At Vellora, we are proud to have a team of seasoned IT professionals who understand what it takes to deliver a quality solution. Our team members have a wealth of experience and expertise in a variety of different areas, including software development, system integration, data migration, and software maintenance and support.</p>
    <p>We understand that delivering a high-quality software solution requires more than just technical expertise. It also requires a deep understanding of the needs and challenges of our clients, and the ability to work closely with them to develop a solution that meets their specific requirements.</p>
  </div>
  <a class="abs btn" style="left:552px;top:2403px"><span class="btn-dot"></span>Read More</a>

  <!-- testimonial -->
  <div class="abs quote-mark">&ldquo;</div>
  <blockquote class="abs quote-text">&ldquo;Lorem ipsum dolor sit amet, consectetur adipiscing elit, sed do eiusmod tempor incididunt ut labore et dolore magna aliqua. Quis ipsum suspendisse ultrices gravida.&rdquo;</blockquote>
  <div class="abs avatar" role="img" aria-label="Portrait photo of the client"></div>
  <div class="abs person"><strong>Maren Tolliver</strong><span>VP Engineering</span></div>

  <!-- blog -->
  <h2 class="abs section-title display" style="top:3218px">Latest Blog Posts</h2>
  <article class="abs post-feature" role="img" aria-label="Photo of a smiling team of colleagues">
    <h3>Lorem ipsum dolor sit amet, consectetur adipiscing elit, sed do</h3>
  </article>
  <article class="abs post-small" style="top:3332px">
    <div class="post-photo" role="img" aria-label="Photo of a woman working on a laptop"></div>
    <div class="post-text"><h4>Lorem ipsum dolor sit amet, consectetur adipiscing elit</h4><p>Lorem ipsum dolor sit amet, consectetur adipiscing elit, sed do eiusmod tempor</p></div>
  </article>
  <article class="abs post-small" style="top:3526px">
    <div class="post-photo" role="img" aria-label="Photo of colleagues meeting at a table"></div>
    <div class="post-text"><h4>Lorem ipsum dolor sit amet, consectetur adipiscing elit</h4><p>Lorem ipsum dolor sit amet, consectetur adipiscing elit, sed do eiusmod tempor</p></div>
  </article>

  <!-- footer -->
  <div class="abs footer-brand"><div class="mark"></div><div class="name">Vellora Consulting</div></div>
  <div class="abs footer-col" style="left:445px">
    <h5>Links</h5>
    <ul><li>Services</li><li>Custom Solution Delivery</li><li>Staff Augmentation</li><li>Why Vellora?</li><li>Vellora Leadership</li></ul>
  </div>
  <div class="abs footer-col" style="left:677px">
    <h5>Support</h5>
    <ul><li>Lorem ipsum dolor</li><li>Rit amet, consectetur</li><li>Adipiscing elit, sed do</li><li>Riusmod temporiunt</li><li>Olabore et dolmagn</li></ul>
  </div>
  <div class="abs footer-col" style="left:903px">
    <h5>Contact</h5>
    <ul><li>Comming Soon.</li></ul>
  </div>
  <div class="abs social"><span></span><span></span><span></span><span></span></div>
  <div class="abs footer-rule"></div>
  <p class="abs copyright">Copyright&copy; 2022 Vellora Consulting. All Rights Reserved.</p>

</div>
</body>
</html>
```